R. K. Belvard & Associates, Inc

Gregor Belvard
Accountant
4219 NW 168th ST
Brackenford, Florida 33998
(305) 555-0187
greg.belvard@quillmarsh.com
Accounting - Tax Preparation Services - Bookkeeping
Side - one business logo on the left and business information on right
On Backside: The logo in the middle and under the logo my company name.

Rounded Corner of the cards
In reference to the logo and cards I need to adjust the circle around the RK and color.

```html
<!DOCTYPE html>
<html lang="en">
<head>
<meta charset="utf-8">
<title>R. K. Belvard &amp; Associates, Inc — Business Cards</title>
<link rel="stylesheet" href="https://fonts.googleapis.com/css2?family=Arimo:wght@400;700&display=swap">
<style>
  :root {
    --bg: #1b1b1b;
    --brand-blue: #0d71bc;
    --paper: #ffffff;
    --ink: #1e1e1e;
    --text-on-blue: #ffffff;
    --radius: 26px;
  }
  * { box-sizing: border-box; margin: 0; padding: 0; }
  html, body {
    width: 1200px; height: 988px; overflow: hidden;
    background: var(--bg);
    font-family: "Arimo", Arial, sans-serif;
  }
  .canvas { position: relative; width: 1200px; height: 988px; }

  .card {
    position: absolute;
    width: 740px; height: 423px;
    border-radius: var(--radius);
    overflow: hidden;
    box-shadow: 0 14px 30px rgba(0,0,0,.55);
  }

  /* Back side */
  .card-back {
    left: 60px; top: 60px;
    background: var(--brand-blue);
    display: flex; flex-direction: column; align-items: center; justify-content: center;
    gap: 34px;
    color: var(--text-on-blue);
  }
  .mark {
    display: flex; align-items: center; justify-content: center;
    border-radius: 50%;
    font-weight: 700;
    letter-spacing: 2px;
  }
  .card-back .mark {
    width: 150px; height: 150px;
    border: 5px solid var(--text-on-blue);
    font-size: 64px;
    color: var(--text-on-blue);
  }
  .company-name {
    font-weight: 700;
    font-size: 38px;
    letter-spacing: .3px;
  }

  /* Front side */
  .card-front {
    left: 400px; top: 505px;
    display: grid; grid-template-columns: 47% 53%;
    background: var(--paper);
  }
  .front-logo {
    display: flex; align-items: center; justify-content: center;
    background: var(--paper);
  }
  .card-front .mark {
    width: 190px; height: 190px;
    border: 7px solid var(--brand-blue);
    font-size: 80px;
    color: var(--ink);
  }
  .front-info {
    background: var(--brand-blue);
    color: var(--text-on-blue);
    padding: 58px 30px 0 34px;
    font-size: 17px;
    line-height: 1.3;
  }
  .person-name {
    font-weight: 700; font-size: 26px; text-transform: uppercase; letter-spacing: .5px;
  }
  .person-role { font-size: 17px; margin-left: 14px; }
  .rule { width: 140px; height: 2px; background: var(--text-on-blue); margin: 10px 0 12px 14px; }
  .address { margin-left: 24px; }
  .contact { list-style: none; margin: 8px 0 0 40px; }
  .contact li { display: flex; align-items: center; gap: 8px; margin-bottom: 2px; }
  .contact svg { width: 18px; height: 18px; flex: none; }
  .rule-services { margin-left: 50px; }
  .services { list-style: none; margin-left: 62px; }
  .services li { margin-bottom: 2px; }
</style>
</head>
<body>
<main class="canvas">

  <section class="card card-back" aria-label="Card back side">
    <div class="mark">RK</div>
    <h1 class="company-name">R. K. Belvard &amp; Associates, Inc</h1>
  </section>

  <section class="card card-front" aria-label="Card front side">
    <div class="front-logo">
      <div class="mark">RK</div>
    </div>
    <div class="front-info">
      <h2 class="person-name">Gregor Belvard</h2>
      <p class="person-role">Accountant</p>
      <div class="rule"></div>
      <p class="address">4219 NW 168th ST<br>Brackenford, Florida 33998</p>
      <ul class="contact">
        <li>
          <svg viewBox="0 0 20 20" aria-hidden="true"><circle cx="10" cy="10" r="9" fill="none" stroke="#fff" stroke-width="1.6"/><path d="M6.5 5.5l2 .2.8 2.2-1.2 1a6 6 0 003 3l1-1.2 2.2.8.2 2c-3.8.6-8.6-4.2-8-8z" fill="#fff"/></svg>
          (305) 555-0187
        </li>
        <li>
          <svg viewBox="0 0 20 20" aria-hidden="true"><circle cx="10" cy="10" r="9" fill="none" stroke="#fff" stroke-width="1.6"/><rect x="5" y="6.5" width="10" height="7" fill="none" stroke="#fff" stroke-width="1.4"/><path d="M5 6.5l5 4 5-4" fill="none" stroke="#fff" stroke-width="1.4"/></svg>
          greg.belvard@quillmarsh.com
        </li>
      </ul>
      <div class="rule rule-services"></div>
      <ul class="services">
        <li>- Accounting</li>
        <li>- Tax Preparation Services</li>
        <li>- Bookkeeping</li>
      </ul>
    </div>
  </section>

</main>
</body>
</html>
```